New website design and logo for BrazeKit.com to help ignite the website sales.

Hi designers,

Brazekit is a new welding brand that is selling welding equipement.

Currently I have around 5 to 10 products. The issue is that the site itself does not do that much of sales. So I have to do something about the seo etc. but that is out of scope for the design.

What is in scope is to comeup with a new logo and website look and feel that is in line with the customers.

men, non professionals, garage, home improvements, perhaps sme ( small mediul entreprice business that want to start in the welding industry.

Products are midrange prices and quality. The look and feel must breath cool stuff, sexy ( women in working cloths carrying welding gloves, other protection gear and weldels)

The wedsite is build in wordpress with the Lumo theme. I am an IT guy myself withhout any creativity in me :( so if you can help me with that that would be great.

Please have a quick look at brazekit.com

Best regards,
Joost

Target Market(s)

non professional welders that do metal work in there garage

Coding

Coded - Design and coding required

Number of Pages Required

3 page

Font styles to use
Sans Serif

Colors
0355a3
ffc214

Requirements
Must have
• I would like to see a new homepage and product page design together with a new logo.
Nice to have
• shop design

```html
<!DOCTYPE html>
<html lang="en">
<head>
<meta charset="utf-8">
<title>Brazekit — Homepage Concepts</title>
<link href="https://fonts.googleapis.com/css2?family=Roboto+Condensed:wght@400;700&family=Roboto:wght@400;500&display=swap" rel="stylesheet">
<style>
:root{
  --blue:#0355a3;
  --blue-bright:#1652c4;
  --yellow:#ffc214;
  --ink:#111111;
  --card:#f8f3f2;
  --stage:#4d4d4d;
  --white:#ffffff;
  --footer:#000000;
  --muted:#d8d8d8;
}
*{box-sizing:border-box;margin:0;padding:0}
html,body{width:1091px;height:1200px;overflow:hidden}
body{background:var(--stage);position:relative;font-family:"Roboto",Arial,sans-serif;color:var(--ink)}
.page{position:absolute;top:11px;width:895px;background:var(--white);transform:scale(.5955);transform-origin:0 0;overflow:hidden}
.page--flat{left:9px}
.page--curved{left:550px}

/* header */
.site-header{height:60px;position:relative;background:var(--white)}
.brand{position:absolute;left:84px;top:14px;display:flex;align-items:center;gap:6px}
.brand__dot{width:24px;height:24px;border-radius:50%;background:var(--yellow)}
.brand__name{font-family:"Roboto Condensed",sans-serif;font-weight:700;font-size:17px;color:var(--blue)}
.nav{position:absolute;top:22px;left:0;font-family:"Roboto Condensed",sans-serif;font-weight:700;font-size:12px}
.nav a{position:absolute;white-space:nowrap;color:var(--ink);text-decoration:none}
.search{position:absolute;left:686px;top:22px}
.cart{position:absolute;left:722px;top:19px;width:88px;height:18px;border:1px solid var(--blue);border-radius:9px;display:flex;align-items:center;font-family:"Roboto Condensed",sans-serif;font-weight:700;font-size:10px;gap:5px}
.cart__count{width:16px;height:16px;border-radius:50%;background:var(--blue);color:var(--white);font-size:8px;display:flex;align-items:center;justify-content:center;margin-left:-1px}

/* hero */
.hero{position:relative;height:415px;background:radial-gradient(ellipse at 55% 45%,#3a7be0 0%,#1b3f9a 30%,#0b1a44 62%,#04070f 100%)}
.page--curved .hero{height:495px;background:none}
.hero__photo{position:absolute;inset:0;background:radial-gradient(ellipse at 55% 45%,#3a7be0 0%,#1b3f9a 30%,#0b1a44 62%,#04070f 100%)}
.hero__curve{position:absolute;left:0;bottom:-2px;width:895px;height:112px}
.hero__title{position:absolute;left:83px;top:138px;font-family:"Roboto Condensed",sans-serif;font-weight:700;font-size:31px;line-height:42px;color:var(--white)}
.page--curved .hero__title{top:136px}
.btn-pill{display:inline-flex;align-items:center;justify-content:center;border-radius:17px;font-family:"Roboto Condensed",sans-serif;font-weight:700;font-size:12px;color:var(--blue)}
.hero .btn-pill{position:absolute;left:85px;top:238px;width:86px;height:34px;background:var(--white)}
.page--curved .hero .btn-pill{top:237px}
.slider-dots{position:absolute;left:800px;top:134px;display:flex;flex-direction:column;gap:9px}
.slider-dots span{width:9px;height:9px;border-radius:50%;background:var(--white)}
.slider-dots span.is-active{background:var(--blue-bright)}

/* products */
.products{position:relative;height:804px}
.page--curved .products{height:807px}
.products__title{position:absolute;left:0;right:0;top:62px;text-align:center;font-family:"Roboto Condensed",sans-serif;font-weight:700;font-size:26px}
.page--curved .products__title{top:59px}
.products__title::after{content:"";display:block;width:56px;height:3px;background:var(--blue-bright);margin:6px auto 0}
.grid{position:absolute;left:87px;top:147px;display:grid;grid-template-columns:repeat(3,233px);gap:23px 13px}
.page--curved .grid{top:143px}
.card{height:283px;background:var(--card);box-shadow:0 1px 5px rgba(0,0,0,.22);text-align:center;padding-top:21px;position:relative}
.card__name{font-family:"Roboto Condensed",sans-serif;font-weight:700;font-size:16px;line-height:18px;min-height:18px}
.card__price{font-size:12px;margin-top:8px}
.card .btn-pill{width:86px;height:34px;border:2px solid var(--blue-bright);margin-top:14px}
.card__media{position:absolute;left:58px;top:133px;width:117px;height:128px;border-radius:10px}
.media--red{background:linear-gradient(160deg,#d33a3a,#6a1717 70%,#222)}
.media--blue{background:linear-gradient(160deg,#c9ced8,#2e66c9 65%,#1d3f8a)}
.media--helmet{background:linear-gradient(160deg,#4a4a50,#1a1a1e 70%,#0d0d10)}
.media--gloves-blue{background:linear-gradient(135deg,#2a2fa8 0 45%,#d89a2a 55%)}
.media--gloves-black{background:linear-gradient(160deg,#3d4436,#1b1f18)}

/* promo */
.promo{position:relative;height:346px;background:radial-gradient(ellipse at 65% 80%,#ff8a1e 0%,#b84a0b 30%,#3a2412 62%,#1a1410 100%)}
.promo__badge{position:absolute;left:88px;top:43px;width:260px;height:260px;border-radius:50%;background:rgba(10,80,185,.9);text-align:center;color:var(--white);padding-top:40px}
.promo__name{font-family:"Roboto Condensed",sans-serif;font-weight:700;font-size:26px}
.promo__text{font-size:12px;line-height:22px;margin-top:8px}
.promo__value{font-family:"Roboto Condensed",sans-serif;font-weight:700;font-size:45px;line-height:50px;margin-top:2px}
.promo .btn-pill{width:106px;height:28px;background:var(--white);font-weight:400;font-size:12px;margin-top:6px;border-radius:14px}

/* footer */
.site-footer{position:relative;height:290px;background:var(--footer);color:var(--white)}
.page--curved .site-footer{height:272px}
.footer-col{position:absolute;top:72px}
.footer-col h4{font-family:"Roboto Condensed",sans-serif;font-weight:700;font-size:11px;margin-bottom:18px}
.footer-col p,.footer-col li{font-size:12px;line-height:22px;list-style:none;color:var(--muted)}
.footer-col li{color:var(--white)}
.cards-accepted{display:flex;gap:5px;margin-top:10px}
.cards-accepted span{width:21px;height:13px;background:#c7c7c7;border-radius:2px}
.newsletter{display:flex;margin-top:0}
.newsletter__field{width:172px;height:32px;background:var(--white);color:var(--ink);font-size:12px;display:flex;align-items:center;padding-left:14px}
.newsletter__send{width:47px;height:32px;background:var(--blue-bright);display:flex;align-items:center;justify-content:center}
.social{display:flex;gap:14px;margin-top:14px}
.social span{width:8px;height:8px;border-radius:50%;background:var(--white)}
.footer-rule{position:absolute;left:83px;right:83px;top:245px;height:1px;background:#262626}
.page--curved .footer-rule{top:230px}
.copyright{position:absolute;left:0;right:0;top:257px;text-align:center;font-size:12px}
.page--curved .copyright{top:254px}
</style>
</head>
<body>

<!-- Concept A: straight hero edge -->
<div class="page page--flat">
  <header class="site-header">
    <div class="brand"><span class="brand__dot"></span><span class="brand__name">Brazekit</span></div>
    <nav class="nav"><a style="left:331px">HOME</a><a style="left:389px">PRODUCTS</a><a style="left:470px">SHOPPING CART</a><a style="left:577px">MY ACCOUNT</a></nav>
    <svg class="search" width="11" height="11" viewBox="0 0 11 11"><circle cx="4.5" cy="4.5" r="3.5" fill="none" stroke="#111" stroke-width="1.6"/><line x1="7" y1="7" x2="10" y2="10" stroke="#111" stroke-width="1.8"/></svg>
    <div class="cart"><span class="cart__count">0</span><svg width="11" height="10" viewBox="0 0 11 10"><rect x="1" y="3" width="9" height="7" fill="#0355a3"/><path d="M3.5 3V2a2 2 0 0 1 4 0v1" fill="none" stroke="#0355a3"/></svg><span>$ 0.00</span><svg width="7" height="5" viewBox="0 0 7 5" style="margin-left:6px"><path d="M0 0h7L3.5 5z" fill="#111"/></svg></div>
  </header>
  <section class="hero" role="img" aria-label="Welder in a helmet working amid blue sparks">
    <h1 class="hero__title">Simple welding of steel and aluminum<br>Get great results with tools that work</h1>
    <span class="btn-pill">Shop Now</span>
    <div class="slider-dots"><span></span><span></span><span class="is-active"></span><span></span><span></span></div>
  </section>
  <section class="products">
    <h2 class="products__title">Our Products</h2>
    <div class="grid">
      <article class="card"><h3 class="card__name">MIG-250P</h3><p class="card__price">€ 795.00</p><span class="btn-pill">Shop Now</span><div class="card__media media--red" role="img" aria-label="Red MIG welding machine"></div></article>
      <article class="card"><h3 class="card__name">MIG-2500</h3><p class="card__price">€ 745.00</p><span class="btn-pill">Shop Now</span><div class="card__media media--blue" role="img" aria-label="Blue and grey MIG welding machine"></div></article>
      <article class="card" style="padding-top:15px"><h3 class="card__name">Welding helmet 180<br>degrees view</h3><p class="card__price">€ 795.00</p><span class="btn-pill" style="margin-top:12px">Shop Now</span><div class="card__media media--helmet" role="img" aria-label="Black welding helmet with purple visor"></div></article>
      <article class="card"><h3 class="card__name">Welding helmet large view</h3><p class="card__price">€ 89.00</p><span class="btn-pill">Shop Now</span><div class="card__media media--helmet" role="img" aria-label="Black welding helmet with large visor"></div></article>
      <article class="card"><h3 class="card__name">Welding gloves Blue</h3><p class="card__price">€ 22.40</p><span class="btn-pill">Shop Now</span><div class="card__media media--gloves-blue" role="img" aria-label="Blue and yellow welding gloves"></div></article>
      <article class="card"><h3 class="card__name">Welding gloves Black</h3><p class="card__price">€ 22.40</p><span class="btn-pill">Shop Now</span><div class="card__media media--gloves-black" role="img" aria-label="Black leather welding gloves"></div></article>
    </div>
  </section>
  <section class="promo" role="img" aria-label="Grinder throwing orange sparks">
    <div class="promo__badge"><div class="promo__name">Brazekit</div><p class="promo__text">Lorem ipsum dolor sit amet, consectetur<br>adipiscing elit, sed do eiusmod</p><div class="promo__value">50%</div><span class="btn-pill">SHOP NOW</span></div>
  </section>
  <footer class="site-footer">
    <div class="footer-col" style="left:85px"><h4>ACCEPTED PAYMENT METHODS</h4><p>Lorem ipsum dolor sit amet,<br>consectetur adipiscing elit, sed<br>do eiusmod tempor incididunt</p><div class="cards-accepted"><span></span><span></span><span></span><span></span><span></span><span></span><span></span></div></div>
    <div class="footer-col" style="left:301px"><h4>QUICK LINK</h4><ul><li>Home</li><li>Products</li><li>Shopping cart</li><li>My account</li></ul></div>
    <div class="footer-col" style="left:422px"><h4>HELP LINK</h4><ul><li>Support / Contact</li><li>Privacy Policies</li><li>Terms of use</li><li>Exchange and Return Policy</li></ul></div>
    <div class="footer-col" style="left:594px"><h4>SUBSCRIBE TO OUR NEWSLETTER</h4><div class="newsletter"><span class="newsletter__field">Enter Your Email</span><span class="newsletter__send"><svg width="14" height="12" viewBox="0 0 14 12"><path d="M0 6L14 0L10 12L7 8z" fill="#fff"/></svg></span></div><div class="social"><span></span><span></span><span></span><span></span></div></div>
    <div class="footer-rule"></div>
    <p class="copyright">© Copyrights 2021 Brazekit &nbsp;| &nbsp;&nbsp;All Rights Reserved</p>
  </footer>
</div>

<!-- Concept B: curved hero edge -->
<div class="page page--curved">
  <header class="site-header">
    <div class="brand"><span class="brand__dot"></span><span class="brand__name">Brazekit</span></div>
    <nav class="nav"><a style="left:331px">HOME</a><a style="left:389px">PRODUCTS</a><a style="left:470px">SHOPPING CART</a><a style="left:577px">MY ACCOUNT</a></nav>
    <svg class="search" width="11" height="11" viewBox="0 0 11 11"><circle cx="4.5" cy="4.5" r="3.5" fill="none" stroke="#111" stroke-width="1.6"/><line x1="7" y1="7" x2="10" y2="10" stroke="#111" stroke-width="1.8"/></svg>
    <div class="cart"><span class="cart__count">0</span><svg width="11" height="10" viewBox="0 0 11 10"><rect x="1" y="3" width="9" height="7" fill="#0355a3"/><path d="M3.5 3V2a2 2 0 0 1 4 0v1" fill="none" stroke="#0355a3"/></svg><span>$ 0.00</span><svg width="7" height="5" viewBox="0 0 7 5" style="margin-left:6px"><path d="M0 0h7L3.5 5z" fill="#111"/></svg></div>
  </header>
  <section class="hero">
    <div class="hero__photo" role="img" aria-label="Welder in a helmet working amid blue sparks"></div>
    <svg class="hero__curve" viewBox="0 0 895 112" preserveAspectRatio="none"><path d="M0 7 Q200 90 447 110 Q640 70 895 0 V112 H0z" fill="#fff"/></svg>
    <h1 class="hero__title">Simple welding of steel and aluminum<br>Get great results with tools that work</h1>
    <span class="btn-pill">Shop Now</span>
    <div class="slider-dots"><span></span><span></span><span class="is-active"></span><span></span><span></span></div>
  </section>
  <section class="products">
    <h2 class="products__title">Our Products</h2>
    <div class="grid">
      <article class="card"><h3 class="card__name">MIG-250P</h3><p class="card__price">€ 795.00</p><span class="btn-pill">Shop Now</span><div class="card__media media--red" role="img" aria-label="Red MIG welding machine"></div></article>
      <article class="card"><h3 class="card__name">MIG-2500</h3><p class="card__price">€ 745.00</p><span class="btn-pill">Shop Now</span><div class="card__media media--blue" role="img" aria-label="Blue and grey MIG welding machine"></div></article>
      <article class="card" style="padding-top:15px"><h3 class="card__name">Welding helmet 180<br>degrees view</h3><p class="card__price">€ 795.00</p><span class="btn-pill" style="margin-top:12px">Shop Now</span><div class="card__media media--helmet" role="img" aria-label="Black welding helmet with purple visor"></div></article>
      <article class="card"><h3 class="card__name">Welding helmet large view</h3><p class="card__price">€ 89.00</p><span class="btn-pill">Shop Now</span><div class="card__media media--helmet" role="img" aria-label="Black welding helmet with large visor"></div></article>
      <article class="card"><h3 class="card__name">Welding gloves Blue</h3><p class="card__price">€ 22.40</p><span class="btn-pill">Shop Now</span><div class="card__media media--gloves-blue" role="img" aria-label="Blue and yellow welding gloves"></div></article>
      <article class="card"><h3 class="card__name">Welding gloves Black</h3><p class="card__price">€ 22.40</p><span class="btn-pill">Shop Now</span><div class="card__media media--gloves-black" role="img" aria-label="Black leather welding gloves"></div></article>
    </div>
  </section>
  <section class="promo" role="img" aria-label="Grinder throwing orange sparks">
    <div class="promo__badge"><div class="promo__name">Brazekit</div><p class="promo__text">Lorem ipsum dolor sit amet, consectetur<br>adipiscing elit, sed do eiusmod</p><div class="promo__value">50%</div><span class="btn-pill">SHOP NOW</span></div>
  </section>
  <footer class="site-footer">
    <div class="footer-col" style="left:83px"><h4>ACCEPTED PAYMENT METHODS</h4><p>Lorem ipsum dolor sit amet,<br>consectetur adipiscing elit, sed<br>do eiusmod tempor incididunt</p><div class="cards-accepted"><span></span><span></span><span></span><span></span><span></span><span></span><span></span></div></div>
    <div class="footer-col" style="left:298px"><h4>QUICK LINK</h4><ul><li>Home</li><li>Products</li><li>Shopping cart</li><li>My account</li></ul></div>
    <div class="footer-col" style="left:419px"><h4>HELP LINK</h4><ul><li>Support / Contact</li><li>Privacy Policies</li><li>Terms of use</li><li>Exchange and Return Policy</li></ul></div>
    <div class="footer-col" style="left:590px"><h4>SUBSCRIBE TO OUR NEWSLETTER</h4><div class="newsletter"><span class="newsletter__field">Enter Your Email</span><span class="newsletter__send"><svg width="14" height="12" viewBox="0 0 14 12"><path d="M0 6L14 0L10 12L7 8z" fill="#fff"/></svg></span></div><div class="social"><span></span><span></span><span></span><span></span></div></div>
    <div class="footer-rule"></div>
    <p class="copyright">© Copyrights 2021 Brazekit &nbsp;| &nbsp;&nbsp;All Rights Reserved</p>
  </footer>
</div>

</body>
</html>
```